nutrition ebook cover

i need a cover for a ebook designed, the book is called velvet ridge so i would like that somewhere on the cover. i would also like the word nutrition followed by my company logo that i have attached below somewhere on the cover( i have attached two logos and would like to see with both separatley), i would like this to be faded into the background if possible, perhaps in a upper or lower corner. i would also like to see options with and without the picture i have attached below. the look I'm going for is professional and clean. this is a fat loss, healthy eating booklet. the winning designer i would like to design the following pages within the book aswell no more than 10 pages, that i will provide all content for, i just need help with putting what i have on pdf in a way that looks professional and cool. this would ideally covered in the rate that is paid for the cover. i also have other booklets i need made so the winning designer will most likely get that work too at a later date for an additional fee of course.

Industry/Entity Type

Nutrition

Requirements
Nice to have
• Outside images are welcomed, happy to purchase any stock images used from a outside source

```html
<!DOCTYPE html>
<html lang="en">
<head>
<meta charset="utf-8">
<title>Velvet Ridge – Nutrition</title>
<link href="https://fonts.googleapis.com/css2?family=Lato:wght@100;300;400&display=swap" rel="stylesheet">
<style>
  :root {
    --band: #231f20;
    --ink-light: #f2f2f2;
    --title-ink: #1c1a19;
    --accent-red: #c0272d;
    --photo-slate: #2b3136;
    --photo-deep: #1d2226;
    --photo-wood: #8c5a34;
    --photo-wood-light: #a8703f;
    --page: #e6e6e6;
  }
  * { box-sizing: border-box; margin: 0; padding: 0; }
  html, body {
    width: 1006px;
    height: 1200px;
    overflow: hidden;
    background: var(--page);
  }
  .cover {
    position: relative;
    width: 1006px;
    height: 1200px;
    background: var(--band);
    font-family: 'Lato', sans-serif;
  }
  .cover__top {
    position: absolute;
    top: 0; left: 0;
    width: 100%;
    height: 206px;
    display: flex;
    align-items: center;
    justify-content: center;
  }
  .brand {
    display: flex;
    align-items: center;
    gap: 16px;
    color: var(--ink-light);
    font-weight: 300;
    font-size: 30px;
    letter-spacing: 0.14em;
    text-transform: uppercase;
  }
  .brand__dot {
    width: 22px;
    height: 22px;
    border-radius: 50%;
    background: var(--ink-light);
  }
  .cover__photo {
    position: absolute;
    top: 206px; left: 0;
    width: 100%;
    height: 748px;
    background:
      radial-gradient(ellipse 30% 42% at 50% 50%, var(--photo-wood-light) 0%, var(--photo-wood) 55%, transparent 100%),
      radial-gradient(ellipse at 50% 50%, var(--photo-slate) 0%, var(--photo-deep) 100%);
  }
  .title {
    position: absolute;
    top: 206px; left: 0;
    width: 100%;
    height: 748px;
    color: var(--title-ink);
  }
  .title__main {
    position: absolute;
    left: 0; right: 0;
    top: 150px;
    text-align: center;
    font-weight: 100;
    font-size: 150px;
    line-height: 1;
    letter-spacing: -0.01em;
  }
  .title__box {
    position: absolute;
    left: 380px;
    top: 330px;
    width: 280px;
    height: 82px;
    border: 2px solid var(--title-ink);
    display: flex;
    align-items: center;
    justify-content: center;
    font-weight: 300;
    font-size: 58px;
    line-height: 1;
    padding-bottom: 6px;
  }
  .cover__bottom {
    position: absolute;
    bottom: 0; left: 0;
    width: 100%;
    height: 246px;
  }
  .label {
    position: absolute;
    top: 48px;
    left: 0; right: 0;
    display: flex;
    align-items: center;
    justify-content: center;
    gap: 20px;
  }
  .label__rule {
    width: 2px;
    height: 40px;
    background: var(--accent-red);
  }
  .label__text {
    color: var(--ink-light);
    font-weight: 300;
    font-size: 32px;
    letter-spacing: 0.22em;
    padding-left: 0.22em;
  }
</style>
</head>
<body>
  <div class="cover">
    <header class="cover__top">
      <div class="brand">
        <span class="brand__dot"></span>
        <span class="brand__name">Kestrel Wellness</span>
      </div>
    </header>

    <div class="cover__photo" role="img" aria-label="Overhead photo of a wooden chopping board on a dark slate table surrounded by fresh vegetables: potatoes, tomatoes, mushrooms, broccoli, carrot, spring onions, turnip, chillies, lemon and olive oil"></div>

    <div class="title">
      <div class="title__main">velvet</div>
      <div class="title__box">ridge</div>
    </div>

    <footer class="cover__bottom">
      <div class="label">
        <span class="label__rule"></span>
        <span class="label__text">nutrition</span>
        <span class="label__rule"></span>
      </div>
    </footer>
  </div>
</body>
</html>
```